依頼詳細
〇 ターゲット
地域の求職者(看護師、理学療法士、作業療法士)

〇 掲載方法
地域の福祉フリーペーの裏表紙(https://k-tomo-ne.jp/pompom/index.html

〇 納期
本当は明日まででしたが、早いと助かります。

〇 内容
添付データを参照ください。
シンプルテイストにロゴとコンセプトから―を絡めていただければと思います。

〇納品データ
トンボ付き入稿データ(PDF、ai.)
印刷機で印刷できるPDFデータ(トンボなし)
記載項目
ロゴ:添付(はな訪問看護ステーション森岡の「飯塚」「iizuka」の文字部分を削除して中央位置の訂正お願いします)
内容:添付
サイズ
A4
ページ数
片面
希望イメージ
シンプル 複雑
単色 カラフル
暗い 明るい
日常 高級
遊び心 厳粛
未来的 伝統的
女性的 男性的
希望する色
赤系
納品ファイル
• イラストレーター形式 (.ai)
補足説明

業務内容がシンプルにまとめられており、応募効果が高そうであると判断しました

短期間でたくさんのご提案ありがとうございました。
また、機会がございましたら、よろしくお願いします。

```html
<!DOCTYPE html>
<html lang="ja">
<head>
<meta charset="utf-8">
<title>訪問看護師 大募集 | はな訪問看護ステーション</title>
<link href="https://fonts.googleapis.com/css2?family=M+PLUS+Rounded+1c:wght@500;800;900&family=Zen+Maru+Gothic:wght@500;700&display=swap" rel="stylesheet">
<style>
  :root {
    --paper: #ffffff;
    --sky-top: #a9c6e6;
    --sky-mid: #cfe0f2;
    --sky-low: #f3f7fc;
    --red: #e2313a;
    --deep-red: #c8202b;
    --pink: #f7b8c2;
    --pink-soft: #fbd9df;
    --ink: #2b2b2b;
    --line: #f2a1ad;
  }
  * { box-sizing: border-box; margin: 0; padding: 0; }
  html, body { width: 888px; height: 1200px; overflow: hidden; background: var(--paper); }
  body { font-family: "Zen Maru Gothic", sans-serif; color: var(--ink); }

  .poster {
    position: absolute; left: 64px; top: 40px; width: 760px; height: 1120px;
    overflow: hidden; background: var(--paper);
  }
  .sky {
    position: absolute; inset: 0;
    background:
      radial-gradient(ellipse 60% 25% at 30% 30%, rgba(255,255,255,.7), transparent 70%),
      radial-gradient(ellipse 50% 20% at 75% 55%, rgba(255,255,255,.6), transparent 70%),
      linear-gradient(180deg, var(--sky-top) 0%, var(--sky-mid) 45%, var(--sky-low) 75%, var(--paper) 92%);
  }

  .badge {
    position: absolute; left: 40px; top: 122px; width: 210px; height: 190px;
    background: var(--pink); border-radius: 36px;
    display: flex; flex-direction: column; align-items: center; justify-content: center;
    font-family: "M PLUS Rounded 1c", sans-serif; color: var(--ink);
  }
  .badge-small { font-size: 28px; font-weight: 800; line-height: 1.1; }
  .badge-big { font-size: 62px; font-weight: 900; color: var(--red); line-height: 1.15; }

  .brand {
    position: absolute; right: 36px; top: 30px; width: 260px;
    display: flex; flex-direction: column; align-items: center; gap: 14px;
  }
  .brand-dot { width: 96px; height: 96px; border-radius: 50%; background: var(--red); }
  .brand-name { font-size: 24px; font-weight: 700; color: var(--deep-red); white-space: nowrap; }

  .headline {
    position: absolute; left: 0; right: 0; top: 315px; text-align: center;
    font-family: "M PLUS Rounded 1c", sans-serif; color: var(--red);
    text-shadow: 0 0 6px #fff, 0 0 2px #fff;
  }
  .headline-role { font-size: 84px; font-weight: 800; letter-spacing: 4px; line-height: 1.1; }
  .headline-main { font-size: 140px; font-weight: 900; letter-spacing: 8px; line-height: 1.2; }

  .also {
    position: absolute; left: 0; right: 0; top: 640px; text-align: center;
    font-family: "M PLUS Rounded 1c", sans-serif; font-weight: 800; font-size: 38px;
  }
  .also .job { color: var(--red); border-bottom: 4px solid var(--red); }

  .hands {
    position: absolute; left: 40px; top: 730px; width: 640px; height: 210px;
    background: linear-gradient(90deg, rgba(247,184,194,.0), rgba(247,184,194,.45) 50%, rgba(247,184,194,.0));
    border-radius: 100px;
  }
  .people {
    position: absolute; left: 50px; top: 880px; width: 220px; height: 220px;
    background: radial-gradient(circle at 50% 55%, var(--pink-soft), rgba(251,217,223,0) 70%);
  }

  .search-box {
    position: absolute; right: 20px; top: 840px; width: 280px; height: 160px;
    background: var(--paper); border: 3px solid var(--line);
    display: flex; flex-direction: column; align-items: center; justify-content: center;
    text-align: center; font-weight: 700;
  }
  .search-site { align-self: flex-start; margin-left: 20px; font-size: 22px; color: var(--red); }
  .search-term { font-size: 22px; color: var(--red); margin-top: 6px; }
  .search-action { align-self: flex-end; margin-right: 20px; font-size: 20px; margin-top: 6px; }

  .contact {
    position: absolute; right: 20px; bottom: 0; width: 280px; height: 112px;
    background: var(--pink-soft); padding: 16px 18px;
    font-size: 15px; line-height: 1.55; font-weight: 500;
  }
</style>
</head>
<body>
  <main class="poster">
    <div class="sky" role="img" aria-label="Photo of a pale blue sky with soft white clouds"></div>

    <div class="badge">
      <span class="badge-small">利用者</span>
      <span class="badge-big">急増</span>
      <span class="badge-small">につき</span>
    </div>

    <div class="brand">
      <span class="brand-dot"></span>
      <span class="brand-name">はな訪問看護ステーション</span>
    </div>

    <h1 class="headline">
      <span class="headline-role">訪問看護師</span><br>
      <span class="headline-main">大募集</span>
    </h1>

    <p class="also">他、<span class="job">理学療法士</span>、<span class="job">作業療法士</span>も募集中</p>

    <div class="hands" role="img" aria-label="Line illustration of two hands reaching toward each other"></div>
    <div class="people" role="img" aria-label="Line illustration of two caregivers"></div>

    <div class="search-box">
      <span class="search-site">jobfind</span>
      <span class="search-term">「はな訪問看護ステーション」</span>
      <span class="search-action">で検索</span>
    </div>

    <address class="contact">
      はな訪問看護ステーション<br>
      森岡市花田西1丁目8-11<br>
      問い合わせ：080-4172-3860（花村）
    </address>
  </main>
</body>
</html>
```